Letterhead and Envelope for Mental Health Business

I need letterhead and envelope designs that will match my business cards. I am attaching a *.pds file of my business card so it can be matched.

Business

```html
<!DOCTYPE html>
<html lang="en">
<head>
<meta charset="UTF-8">
<title>Brook Counseling – Envelope</title>
<link href="https://fonts.googleapis.com/css2?family=Roboto+Condensed:wght@400;700&display=swap" rel="stylesheet">
<style>
  :root {
    --paper: #ffffff;
    --ink: #1a1a1a;
    --brand-blue: #2b5d9b;
    --brand-green: #3fae49;
  }
  html, body {
    margin: 0;
    padding: 0;
    overflow: hidden;
    background: var(--paper);
  }
  .envelope {
    position: relative;
    width: 1200px;
    height: 600px;
    background: var(--paper);
    font-family: "Roboto Condensed", "Arial Narrow", sans-serif;
    overflow: hidden;
  }
  .brand {
    position: absolute;
    left: 44px;
    top: 56px;
    display: flex;
    align-items: center;
    gap: 12px;
  }
  .brand-dot {
    width: 62px;
    height: 62px;
    border-radius: 50%;
    background: var(--brand-green);
    flex: none;
  }
  .brand-name {
    margin: 0;
    color: var(--brand-blue);
    font-weight: 700;
    font-size: 34px;
    line-height: 1;
    letter-spacing: 0.5px;
  }
  .return-address {
    position: absolute;
    left: 320px;
    top: 60px;
    margin: 0;
    font-style: normal;
    color: var(--ink);
    font-size: 20px;
    line-height: 1.55;
  }
  .recipient-window {
    position: absolute;
    left: 156px;
    top: 287px;
    width: 535px;
    height: 228px;
    box-sizing: border-box;
    border: 15px solid var(--brand-green);
  }
</style>
</head>
<body>
  <main class="envelope">
    <div class="brand">
      <span class="brand-dot" aria-hidden="true"></span>
      <p class="brand-name">Brook<br>Counseling</p>
    </div>
    <address class="return-address">
      If undeliverable, return to:<br>
      Elm Avenue 48<br>
      8213 LAKETOWN, USA
    </address>
    <div class="recipient-window" aria-label="Recipient address area"></div>
  </main>
</body>
</html>
```